" Estamos a vinte anos no mercado, porem somos de porte pequeno em relação ao mercado. Fazemos abertura/encerramento de empresas, parte contábil, fiscal e departamento pessoal. Além de assessorar o cliente em duvidas corriqueiras que venham a sugir. "

```html
<!DOCTYPE html>
<html lang="pt-BR">
<head>
<meta charset="utf-8">
<title>Verani – cartões de visita</title>
<link href="https://fonts.googleapis.com/css2?family=Arimo:wght@400;700&display=swap" rel="stylesheet">
<style>
  :root {
    --navy: #1d3f5f;
    --mist: #aab6c3;
    --paper: #ffffff;
    --board-line: #c9c9c9;
    --muted: #6d7f91;
  }
  html, body {
    margin: 0;
    padding: 0;
    width: 1200px;
    height: 1200px;
    overflow: hidden;
    background: var(--paper);
    font-family: "Arimo", Arial, sans-serif;
  }
  .board {
    position: absolute;
    left: 5px;
    top: 53px;
    width: 1188px;
    height: 1092px;
    border: 2px solid var(--board-line);
    box-sizing: border-box;
  }
  .card {
    position: absolute;
    background: var(--navy);
    color: var(--paper);
  }
  .card-front {
    left: 336px;
    top: 235px;
    width: 713px;
    height: 216px;
  }
  .accent-disc {
    position: absolute;
    left: 120px;
    top: 215px;
    width: 270px;
    height: 270px;
    border-radius: 50%;
    background: var(--mist);
    border: 8px solid var(--paper);
    box-sizing: border-box;
  }
  .brand {
    display: flex;
    align-items: center;
    gap: 10px;
  }
  .brand-dot {
    width: 22px;
    height: 22px;
    border-radius: 50%;
    background: var(--mist);
  }
  .brand-name {
    font-weight: 700;
    letter-spacing: 1px;
  }
  .card-front .brand {
    position: absolute;
    right: 40px;
    top: 50px;
  }
  .card-front .brand-name {
    font-size: 34px;
    color: var(--paper);
  }
  .contact {
    position: absolute;
    margin: 0;
    text-align: right;
    font-style: normal;
  }
  .contact span { display: block; }
  .card-front .contact {
    right: 40px;
    top: 120px;
    font-size: 17px;
    line-height: 21px;
  }
  .card-back {
    left: 149px;
    top: 715px;
    width: 895px;
    height: 221px;
  }
  .card-back .brand-panel {
    position: absolute;
    left: 19px;
    top: 0;
    width: 324px;
    height: 100%;
    background: var(--paper);
    display: flex;
    align-items: center;
    justify-content: center;
  }
  .card-back .brand-name {
    font-size: 40px;
    color: var(--navy);
  }
  .card-back .brand-dot {
    width: 30px;
    height: 30px;
    background: var(--muted);
  }
  .card-back .contact {
    right: 12px;
    top: 62px;
    font-size: 24px;
    line-height: 27px;
  }
</style>
</head>
<body>
  <div class="board"></div>

  <section class="card card-front" aria-label="Frente do cartão">
    <div class="brand">
      <span class="brand-dot"></span>
      <span class="brand-name">Verani</span>
    </div>
    <address class="contact">
      <span>(00)0000-0000</span>
      <span>contato@veraniexemplo.com</span>
      <span>rua sem nome,00</span>
      <span>bairro sem nome , cidade sem nome</span>
    </address>
  </section>
  <div class="accent-disc" aria-hidden="true"></div>

  <section class="card card-back" aria-label="Verso do cartão">
    <div class="brand-panel">
      <div class="brand">
        <span class="brand-dot"></span>
        <span class="brand-name">Verani</span>
      </div>
    </div>
    <address class="contact">
      <span>(00)0000-0000</span>
      <span>contato@veraniexemplo.com</span>
      <span>rua sem nome,00</span>
      <span>bairro sem nome , cidade sem nome</span>
    </address>
  </section>
</body>
</html>
```